Yard Sign Design Needed

Yard sign needed for mowing & landscaping company. Would like to use the top logo with black background which is attached. Would like MOWING to be in large standout letters. The word "landscaping" can be smaller and more artistic or omitted. Will need room for phone number once design is approved. The phone number will need to stand out and look identical/similar to the word 'MOWING"

```html
<!DOCTYPE html>
<html lang="en">
<head>
<meta charset="utf-8">
<title>Brenlow Contractors – Mowing Yard Sign</title>
<link rel="stylesheet" href="https://fonts.googleapis.com/css2?family=Anton&family=Oswald:wght@500;700&family=Ruge+Boogie&display=swap">
<style>
  :root {
    --sign-black: #060608;
    --leaf-light: #f4f8ea;
    --leaf-green: #a3cf3b;
    --leaf-olive: #77903a;
    --paper-white: #ffffff;
    --ink: #111111;
  }
  * { margin: 0; padding: 0; box-sizing: border-box; }
  html, body {
    width: 1200px;
    height: 720px;
    overflow: hidden;
    background: var(--paper-white);
  }
  .canvas {
    position: relative;
    width: 1200px;
    height: 720px;
  }
  .yard-sign {
    position: absolute;
    left: 384px;
    top: 40px;
    width: 432px;
    height: 640px;
  }
  .accent-stripe {
    position: absolute;
    left: 0;
    top: 0;
    width: 432px;
    height: 12px;
    background: linear-gradient(90deg, var(--leaf-light) 0%, var(--leaf-green) 45%, var(--leaf-olive) 100%);
  }
  .sign-panel {
    position: absolute;
    left: 0;
    top: 22px;
    width: 432px;
    height: 618px;
    background: var(--sign-black);
    overflow: hidden;
  }
  .panel-shapes {
    position: absolute;
    inset: 0;
  }
  .company-name {
    position: absolute;
    left: 0;
    top: 96px;
    width: 100%;
    text-align: center;
    font-family: "Oswald", sans-serif;
    font-weight: 500;
    color: var(--paper-white);
    line-height: 1.1;
  }
  .company-name .name-row {
    display: flex;
    align-items: center;
    justify-content: center;
    gap: 12px;
    font-size: 44px;
    letter-spacing: 3px;
  }
  .company-name .brand-square {
    width: 26px;
    height: 26px;
    background: var(--leaf-green);
  }
  .company-name .name-sub {
    display: block;
    font-size: 22px;
    letter-spacing: 4px;
    margin-top: 6px;
  }
  .service-main {
    position: absolute;
    left: 0;
    top: 282px;
    width: 100%;
    text-align: center;
    font-family: "Anton", sans-serif;
    font-size: 104px;
    line-height: 1;
    letter-spacing: 2px;
    color: var(--ink);
  }
  .service-sub {
    position: absolute;
    left: 0;
    top: 392px;
    width: 100%;
    text-align: center;
    font-family: "Ruge Boogie", cursive;
    font-size: 64px;
    line-height: 1;
    color: var(--ink);
  }
  .phone-number {
    position: absolute;
    left: 0;
    top: 522px;
    width: 100%;
    text-align: center;
    font-family: "Oswald", sans-serif;
    font-weight: 700;
    font-size: 66px;
    line-height: 1.2;
    letter-spacing: 1px;
    color: var(--paper-white);
  }
</style>
</head>
<body>
<main class="canvas">
  <section class="yard-sign">
    <div class="accent-stripe"></div>
    <div class="sign-panel">
      <svg class="panel-shapes" width="432" height="618" viewBox="0 0 432 618" aria-hidden="true">
        <defs>
          <linearGradient id="leafGradient" x1="0" y1="0" x2="1" y2="0">
            <stop offset="0" stop-color="var(--leaf-light)"/>
            <stop offset="0.45" stop-color="var(--leaf-green)"/>
            <stop offset="1" stop-color="var(--leaf-olive)"/>
          </linearGradient>
        </defs>
        <polygon class="service-banner" points="0,270 432,270 432,460 216,510 0,460" fill="url(#leafGradient)"/>
        <polygon class="banner-edge" points="0,460 216,510 432,460 432,476 216,526 0,476" fill="var(--paper-white)"/>
      </svg>

      <div class="company-name">
        <span class="name-row"><span class="brand-square"></span>BRENLOW</span>
        <span class="name-sub">CONTRACTORS LLC</span>
      </div>

      <h1 class="service-main">MOWING</h1>
      <p class="service-sub">landscaping</p>
      <p class="phone-number">98 765 432</p>
    </div>
  </section>
</main>
</body>
</html>
```